Billboard design - consider what a billboard is

Design a billboard using my logo - Billboard is 6m x 3m
A Billboard is advertising for my company that is on a big sign.

Has to be clean and easy to read, and ideally highlights that we are Residential and Commercial builders.

Keep it clean and easy to read

The contact number for the board is

022 583 7092
www.harbourframeworks.co.nz
info@harbourframeworks.co.nz

Doesnt have to have all contact details if it doesnt fit

Has to catch peoples attention to contact us if they need a builder

Can you please change the sign to be all white writing, with black background ?
Updates

Please consider what a billboard is...

The design needs to be suitable for a billboard..

Target Market(s)

people driving past

Industry/Entity Type

Construction

Logo Text

Wellington Builder, website email address, contact number

Colors
0054AA
0677BA
7BADD7
CADEEF
E8F1F8

Requirements
Must have
• Easy to read
Nice to have
• easy to read, can clearly see contact details

```html
<!DOCTYPE html>
<html lang="en">
<head>
<meta charset="utf-8">
<title>Harbour Frameworks Billboard</title>
<link rel="stylesheet" href="https://fonts.googleapis.com/css2?family=Montserrat:wght@600;700&display=swap">
<style>
  :root {
    --page: #ffffff;
    --board: #000000;
    --frame: #111111;
    --accent: #0677ba;
    --text: #ffffff;
    --icon: #ffffff;
  }
  * { margin: 0; padding: 0; box-sizing: border-box; }
  html, body {
    width: 1200px;
    height: 919px;
    overflow: hidden;
    background: var(--page);
  }
  .billboard {
    position: absolute;
    left: 30px;
    top: 174px;
    width: 1140px;
    height: 572px;
    background: var(--board);
    border: 4px solid var(--frame);
    font-family: "Montserrat", sans-serif;
    color: var(--text);
  }
  .brand {
    position: absolute;
    right: 40px;
    top: 22px;
    display: flex;
    align-items: flex-start;
    gap: 24px;
  }
  .brand-square {
    width: 70px;
    height: 70px;
    margin-top: 22px;
    background: var(--accent);
  }
  .brand-name {
    font-size: 106px;
    font-weight: 700;
    line-height: 1.02;
    letter-spacing: -1px;
    text-align: right;
    white-space: nowrap;
  }
  .tagline {
    position: absolute;
    right: 40px;
    top: 252px;
    padding-top: 8px;
    border-top: 4px solid var(--accent);
    font-size: 27px;
    font-weight: 600;
    letter-spacing: 1px;
    text-transform: uppercase;
    white-space: nowrap;
  }
  .accent-bar {
    position: absolute;
    left: 4px;
    top: 318px;
    width: 22px;
    height: 183px;
    background: var(--accent);
  }
  .contact-row {
    position: absolute;
    left: 46px;
    display: flex;
    align-items: center;
    gap: 18px;
    white-space: nowrap;
  }
  .contact-row svg { flex: none; }
  .row-phone { top: 322px; }
  .row-web { top: 400px; }
  .row-mail { top: 462px; }
  .phone-number {
    font-size: 54px;
    font-weight: 700;
    line-height: 1;
  }
  .contact-text {
    font-size: 30px;
    font-weight: 600;
    line-height: 1;
  }
</style>
</head>
<body>
  <section class="billboard">
    <div class="brand">
      <span class="brand-square"></span>
      <span class="brand-name">Harbour<br>Frameworks</span>
    </div>

    <div class="tagline">Residential &amp; Commercial Builders</div>

    <span class="accent-bar"></span>

    <div class="contact-row row-phone">
      <svg width="44" height="50" viewBox="0 0 24 24" aria-hidden="true">
        <path d="M6.6 2.5c.6-.4 1.3-.2 1.7.4l2 3.2c.3.6.2 1.3-.3 1.7l-1.3 1c.7 2.3 2 4.4 3.9 6.2l1.4-.9c.5-.4 1.3-.3 1.7.2l2.4 2.8c.4.5.4 1.3-.1 1.7l-1.5 1.4c-.8.7-2 .9-3 .4C8.6 18.6 5 13.9 4.2 8.8 4 7.7 4.4 6.6 5.2 5.9z" fill="none" stroke="var(--icon)" stroke-width="1.8" stroke-linejoin="round"/>
      </svg>
      <span class="phone-number">022 583 7092</span>
    </div>

    <div class="contact-row row-web">
      <svg width="44" height="44" viewBox="0 0 24 24" aria-hidden="true">
        <g fill="none" stroke="var(--icon)" stroke-width="1.4">
          <circle cx="12" cy="12" r="10"/>
          <ellipse cx="12" cy="12" rx="4.5" ry="10"/>
          <line x1="2" y1="12" x2="22" y2="12"/>
          <path d="M3.8 7h16.4M3.8 17h16.4"/>
        </g>
      </svg>
      <span class="contact-text">www.harbourframeworks.co.nz</span>
    </div>

    <div class="contact-row row-mail">
      <svg width="46" height="34" viewBox="0 0 28 20" aria-hidden="true">
        <g fill="none" stroke="var(--icon)" stroke-width="1.6" stroke-linejoin="round">
          <rect x="1" y="1" width="26" height="18"/>
          <path d="M1 1l13 10 13-10M1 19l9.5-9M27 19l-9.5-9"/>
        </g>
      </svg>
      <span class="contact-text">info@harbourframeworks.co.nz</span>
    </div>
  </section>
</body>
</html>
```